business cards for Tramvex
Tramvexa
business cards for Tramvex - Government
Modern
R.K.Dunmore
914 E Harlan Avenue, Suite 215 Fort Worth, TX 76102
rdunmore@tramvexa-mail.com
www.tramvexa-site.com
need to be able to create cards for other people- the backside is logo only- the front needs my name then tramvexa with address email phone number and website- please put logo on front side as well. colors can be red/white/blue/ black or any combination
big version of logo and possibly ability to write on it- this may not work out well so if it doesn't then don't do it.

```html
<!DOCTYPE html>
<html lang="en">
<head>
<meta charset="utf-8">
<title>Tramvexa Business Cards</title>
<link href="https://fonts.googleapis.com/css2?family=Montserrat:wght@400;600;700&display=swap" rel="stylesheet">
<style>
  :root {
    --backdrop: #2b2d31;
    --card-white: #ffffff;
    --navy: #2c3e66;
    --red: #9b2230;
    --ink: #3a3d45;
    --muted: #6a6e78;
  }
  * { margin: 0; padding: 0; box-sizing: border-box; }
  html, body {
    width: 1200px; height: 698px; overflow: hidden;
    background: var(--backdrop);
    font-family: "Montserrat", sans-serif;
  }
  .card-set {
    position: relative; width: 1200px; height: 698px;
    display: flex; align-items: center; justify-content: center; gap: 50px;
  }
  .card {
    position: relative; width: 525px; height: 300px;
    background: var(--card-white); border-radius: 14px; overflow: hidden;
  }
  .brand { display: flex; align-items: center; gap: 10px; }
  .brand-mark { width: 26px; height: 26px; background: var(--navy); }
  .brand-name { font-weight: 700; color: var(--navy); letter-spacing: 1px; }

  /* back side */
  .card-back .brand { position: absolute; left: 0; right: 0; top: 98px; justify-content: center; }
  .card-back .brand-mark { width: 38px; height: 38px; }
  .card-back .brand-name { font-size: 34px; }
  .card-back .website {
    position: absolute; left: 0; right: 0; top: 200px; text-align: center;
    font-size: 12px; letter-spacing: 2.5px; color: var(--ink);
  }

  /* front side */
  .front-shape { position: absolute; inset: 0; }
  .card-front .brand { position: absolute; left: 34px; top: 50px; }
  .card-front .brand-name { font-size: 24px; }
  .person { position: absolute; left: 34px; top: 170px; }
  .person-name { font-size: 14px; font-weight: 700; color: var(--navy); letter-spacing: 1px; }
  .person-title { font-size: 9px; font-weight: 600; color: var(--red); letter-spacing: 1.5px; margin-top: 3px; }
  .address {
    position: absolute; left: 34px; top: 254px;
    font-size: 9px; line-height: 14px; color: var(--card-white); letter-spacing: .5px;
  }
  .contact-list {
    position: absolute; right: 20px; top: 56px; list-style: none;
  }
  .contact-list li {
    display: flex; align-items: center; justify-content: flex-end; gap: 8px;
    font-size: 9px; color: var(--card-white); height: 19px; letter-spacing: .3px;
  }
  .contact-icon { width: 12px; height: 12px; flex: none; }
</style>
</head>
<body>
<main class="card-set">
  <section class="card card-back" aria-label="Card back">
    <div class="brand">
      <span class="brand-mark"></span>
      <span class="brand-name">TRAMVEXA</span>
    </div>
    <p class="website">www.tramvexa-site.com</p>
  </section>

  <section class="card card-front" aria-label="Card front">
    <svg class="front-shape" viewBox="0 0 525 300" width="525" height="300">
      <path fill="var(--red)" d="M286,0 C326,112 276,226 0,234 L0,300 L525,300 L525,0 Z"/>
      <path fill="var(--card-white)" d="M292,0 C332,114 282,230 0,238 L0,300 L525,300 L525,0 Z"/>
      <path fill="var(--navy)" d="M300,0 C340,116 290,234 0,242 L0,300 L525,300 L525,0 Z"/>
    </svg>
    <div class="brand">
      <span class="brand-mark"></span>
      <span class="brand-name">TRAMVEXA</span>
    </div>
    <div class="person">
      <p class="person-name">R.K. DUNMORE</p>
      <p class="person-title">PRESIDENT</p>
    </div>
    <p class="address">914 E Harlan Avenue, Suite 215<br>Fort Worth, TX 76102</p>
    <ul class="contact-list">
      <li>817 555 0142
        <svg class="contact-icon" viewBox="0 0 12 12"><path fill="#fff" d="M2.5 1 L4.5 1 L5 3.5 L3.8 4.5 C4.5 6 6 7.5 7.5 8.2 L8.5 7 L11 7.5 L11 9.5 C11 10.3 10.3 11 9.5 11 C5 11 1 7 1 2.5 C1 1.7 1.7 1 2.5 1 Z"/></svg>
      </li>
      <li>817 555 0143
        <svg class="contact-icon" viewBox="0 0 12 12"><rect x="1.5" y="1" width="9" height="10" rx="1.2" fill="none" stroke="#fff"/><line x1="3.5" y1="4" x2="8.5" y2="4" stroke="#fff"/><line x1="3.5" y1="6.5" x2="8.5" y2="6.5" stroke="#fff"/></svg>
      </li>
      <li>rdunmore@tramvexa-mail.com
        <svg class="contact-icon" viewBox="0 0 12 12"><rect x="1" y="2.5" width="10" height="7" fill="none" stroke="#fff"/><path d="M1 2.5 L6 6.5 L11 2.5" fill="none" stroke="#fff"/></svg>
      </li>
      <li>www.tramvexa-site.com
        <svg class="contact-icon" viewBox="0 0 12 12"><circle cx="6" cy="6" r="5" fill="none" stroke="#fff"/><ellipse cx="6" cy="6" rx="2.2" ry="5" fill="none" stroke="#fff"/><line x1="1" y1="6" x2="11" y2="6" stroke="#fff"/></svg>
      </li>
    </ul>
  </section>
</main>
</body>
</html>
```